Wordpress Design Project - IT Consulting Services Web Site

Our are starting a new technology services company. We will provide services in software implementation and business intelligence.

We need a beautiful Wordpress web site design. We need a design for the homepage, and one interior content page.

The site must have a very professional and polished look and feel. What I have suggested below are things that I think work, but I am not a designer and I am open to your professional opinions. Please be willing to use your best judgment.

The homepage should have the following elements:
- A Header Area that includes:
o The company logo, and
o navigation (consistent with the interior page)
o a social media link section that includes rss feeds, youtube, facebook, linkedin and tweets
- A Body that includes:
o A slider
o An area that features up to six of the most recent or important posts including a thumbnail and small picture, a title, and a short excerpt for each.
o An area for around 100 words of text and an image
- A footer that includes:
o The company logo
o Contact information

The interior page is relatively simple. It should include the same navigation element as the homepage, and accommodate a one column text layout.

The current site …
You can visit the current site at www.korvelpath.com I built the current site using the “Velthor Quick Pane” premium theme. If you visit this site you get a sense of some of the things I am talking about, but there are things that I do not like about the current site. Here’s what I like and what I don’t like.

What I like about the current site:
- It is reactive – it adapts to the size of the viewing browser
- It has a “metro” feel to it. The company will have an association with Microsoft and having a “metro” theme is a plus, but not a requirement.
- It is different without being hard to navigate – the site the slider is from the “glide cascade widget”, the posts are represented with tiles and rearrange themselves when a topic is selected.

What I don’t like:
- The site lacks a cohesive feel – it feels to me like a bunch of different elements without a single theme that pulls everything together.
- It is not aesthetically appealing to me.
- The tiles in the post section are too big.
- I don’t like the white background – I would prefer a background color and ideally a background that somehow incorporates the graphic in the logo.

About themes
As I said, I used a Velthor theme in my design. I will be happy to continue using this theme, or would be willing to buy a new premium theme, so long as the cost is less than $100 U.S.

Site Map:
What we do
ERP Implementation
Business Intelligence
Who we are
What’s different about us
Principles
Mission, Vision, Values
Actions
How we work
What’s Different About Us
Blogs
What Papers
Presentations
Join
What we are looking for
What are you looking for?
Benefits
Context
Updates

Regarding Pictures
Please do not feel you need to use any of the pictures currently on the site.  Use whatever pictures you feel look best.  Comps are okay. 

It is not necessary to use any of the content on the current site - you do not need to use either the pictures or the text.  Please feel free to use pictures of your choice (comps okay), and/or lorem text.

The top level navigation is the navigation I would like.

Hello all,

Since this is a Wordpress project, it goes without saying I will need to implement this design in Wordpress.  It is not absolutely necessary that a design that matches an existing template (free or not), but a design that does will have an advantage over a design which requires that a new template be coded from scratch.

Thank you.

Target Market(s)

Business executives and potential employees

Industry/Entity Type

Software

Requirements
Nice to have
• It would be nice if the site was reactive.

```html
<!DOCTYPE html>
<html lang="en">
<head>
<meta charset="utf-8">
<title>KorvelPath — Software Implementation &amp; Business Intelligence</title>
<link rel="stylesheet" href="https://fonts.googleapis.com/css2?family=Roboto:wght@300;400&display=swap">
<style>
:root{
  --blue:#0a93d5;
  --blue-soft:#3aa8dc;
  --page:#f4f4f4;
  --ink:#555759;
  --ink-soft:#8a8c8e;
  --tile-gray:#5f6062;
  --footer:#a6a8ab;
  --white:#ffffff;
}
*{box-sizing:border-box;margin:0;padding:0}
html,body{width:1200px;height:1178px;overflow:hidden}
body{position:relative;background:var(--page);font-family:"Roboto",Helvetica,Arial,sans-serif;font-weight:300;color:var(--ink)}
.abs{position:absolute}

/* header */
.brand{left:200px;top:52px;display:flex;align-items:center;gap:8px}
.brand-name{font-size:27px;font-weight:300;color:#8d8f91;letter-spacing:-1px}
.brand-dot{width:14px;height:14px;border-radius:50%;background:var(--blue)}
.nav-item{top:50px}
.nav-main{font-size:27px;color:var(--blue);line-height:1;display:flex;align-items:center;gap:10px}
.nav-main svg{width:14px;height:9px}
.nav-sub{font-size:11.5px;color:#6a6c6e;margin-top:4px}
.nav-sep{top:56px;width:1px;height:34px;background:#d6d6d6}

.toolbar{left:200px;top:114px;width:801px;height:49px;background:var(--blue)}
.search{left:9px;top:9px;width:292px;height:32px;background:var(--white);display:flex;align-items:center;justify-content:space-between;padding:0 6px 0 13px;font-size:14px;color:#b5b5b5}
.social{position:absolute;width:32px;height:32px;border-radius:50%;background:var(--white);top:8px}

/* hero */
.hero{left:0;top:182px;width:1200px;height:395px;background:linear-gradient(90deg,#d9dcdc 0%,#e9ebea 30%,#d3d6d5 55%,#c9cccb 70%,#b7a897 88%,#d4d6d6 100%)}
.hero-card{left:200px;top:264px;width:296px;height:226px;background:linear-gradient(135deg,#3fb0e3,#1f97d2);color:var(--white);padding:12px 15px}
.hero-card .small{font-size:32px;line-height:32px;letter-spacing:-1px}
.hero-card .big{font-size:51px;line-height:49px;letter-spacing:-2px}
.read-more{display:flex;align-items:center;gap:8px;font-size:22px;margin-top:10px}

/* features */
.feature-photo{left:200px;top:600px;width:208px;height:255px;background:linear-gradient(180deg,#cfd4d8,#e8eaec 60%,#c8ccd0)}
.feature{left:428px;width:560px}
.feature .kicker{font-size:10.5px;color:var(--ink-soft)}
.feature h2{font-weight:300;font-size:29px;color:var(--blue);letter-spacing:-.5px;margin-top:1px}
.feature p{font-size:14.4px;line-height:19px;margin-top:4px;color:#5b5d5f}
.divider{left:428px;top:719px;width:568px;height:1px;background:#d9d9d9}

/* recent posts */
.posts-title{left:203px;top:884px;font-size:24px;color:var(--ink)}
.filters{left:380px;top:890px;font-size:15.5px;color:var(--ink-soft);display:flex;gap:10px}
.filters .on{color:var(--blue)}
.tile{top:928px;height:81px;color:var(--white);overflow:hidden}
.tile.gray{background:var(--tile-gray)}
.tile.blue{background:var(--blue)}
.tile-line{position:absolute;white-space:nowrap}

/* footer */
.footer{left:0;top:1028px;width:1200px;height:150px;background:var(--footer);color:var(--white)}
.footer h3{font-weight:300;font-size:23px}
.footer p{font-size:10.5px;line-height:14px}
.foot-social{position:absolute;width:29px;height:29px;border-radius:50%;background:#c9cacc;top:107px}
</style>
</head>
<body>

<header>
  <div class="abs brand"><span class="brand-name">KorvelPath</span><span class="brand-dot"></span></div>

  <nav>
    <div class="abs nav-item" style="left:506px"><div class="nav-main">what<svg viewBox="0 0 14 9"><path d="M1 1l6 6 6-6" fill="none" stroke="#0a93d5" stroke-width="1.5"/></svg></div><div class="nav-sub">What we do</div></div>
    <div class="abs nav-sep" style="left:597px"></div>
    <div class="abs nav-item" style="left:615px"><div class="nav-main">who<svg viewBox="0 0 14 9"><path d="M1 1l6 6 6-6" fill="none" stroke="#0a93d5" stroke-width="1.5"/></svg></div><div class="nav-sub">Who we are</div></div>
    <div class="abs nav-sep" style="left:701px"></div>
    <div class="abs nav-item" style="left:718px"><div class="nav-main">how<svg viewBox="0 0 14 9"><path d="M1 1l6 6 6-6" fill="none" stroke="#0a93d5" stroke-width="1.5"/></svg></div><div class="nav-sub">How we work</div></div>
    <div class="abs nav-sep" style="left:808px"></div>
    <div class="abs nav-item" style="left:826px"><div class="nav-main">join<svg viewBox="0 0 14 9"><path d="M1 1l6 6 6-6" fill="none" stroke="#0a93d5" stroke-width="1.5"/></svg></div><div class="nav-sub">Join us</div></div>
    <div class="abs nav-sep" style="left:902px"></div>
    <div class="abs nav-item" style="left:919px"><div class="nav-main">contact</div><div class="nav-sub">Contact us</div></div>
  </nav>

  <div class="abs toolbar">
    <div class="abs search"><span>Search</span>
      <svg width="26" height="26" viewBox="0 0 26 26"><circle cx="13" cy="13" r="11" fill="none" stroke="#0a93d5" stroke-width="2"/><path d="M7 13h11M13 8l5 5-5 5" fill="none" stroke="#0a93d5" stroke-width="2.2"/></svg>
    </div>
    <span class="social" style="left:598px" aria-label="Social link"></span>
    <span class="social" style="left:637px" aria-label="Social link"></span>
    <span class="social" style="left:676px" aria-label="Social link"></span>
    <span class="social" style="left:715px" aria-label="Social link"></span>
    <span class="social" style="left:754px" aria-label="Social link"></span>
  </div>
</header>

<main>
  <section class="abs hero" role="img" aria-label="Photo of a businessman in a suit holding a tablet in a bright, blurred office"></section>
  <div class="abs hero-card">
    <div class="small">software<br>implementation &amp;</div>
    <div class="big">business<br>intelligence</div>
    <div class="read-more"><svg width="20" height="20" viewBox="0 0 20 20"><circle cx="10" cy="10" r="9" fill="none" stroke="#fff" stroke-width="1.5"/><path d="M5 10h9M10 6l4 4-4 4" fill="none" stroke="#fff" stroke-width="1.6"/></svg>read more</div>
  </div>

  <div class="abs feature-photo" role="img" aria-label="Photo of a smiling consultant with colleagues in an office"></div>

  <article class="abs feature" style="top:601px">
    <div class="kicker">People, Processes and Tools</div>
    <h2>Putting People First</h2>
    <p>Every services firm is made up of people, processes and tools. At Korvel Path, we put people first, tailoring everything we do to find, hire, train, and keep the very best people. Because once you have the best people everything else follows.</p>
  </article>
  <div class="abs divider"></div>
  <article class="abs feature" style="top:731px">
    <div class="kicker">Korvel Path</div>
    <h2>What’s the idea?</h2>
    <p>The idea is an old one but a great one. Elias Marlow Penn was an American writer credited with creating the phrase “The American Dream”. It’s the idea that your success should depend on your ability and achievements, not on where you started out. It’s an idea we try to live up to.</p>
  </article>

  <h2 class="abs posts-title" style="font-weight:300">Recent Posts</h2>
  <div class="abs filters"><span class="on">all</span>|<span>identity</span>|<span>people</span>|<span>principles</span>|<span>services</span>|<span>thought leadership</span>|<span>values</span></div>

  <div class="abs tile gray" style="left:201px;width:81px"><div class="tile-line" style="left:6px;top:39px;font-size:21px;line-height:20px">Growth</div><div class="tile-line" style="left:7px;top:62px;font-size:12.5px">is essential</div></div>
  <div class="abs tile blue" style="left:290px;width:172px"><div class="tile-line" style="left:7px;top:2px;font-size:48px;letter-spacing:-2px">ERP</div><div class="tile-line" style="left:8px;top:53px;font-size:21px">Implementation</div></div>
  <div class="abs tile gray" style="left:470px;width:81px"><div class="tile-line" style="left:6px;top:43px;font-size:11px">Respect the</div><div class="tile-line" style="left:6px;top:52px;font-size:21px">journey</div></div>
  <div class="abs tile blue" style="left:560px;width:170px"><div class="tile-line" style="left:9px;top:-2px;font-size:36px;letter-spacing:-1px">expertise</div><div class="tile-line" style="left:10px;top:39px;font-size:12.5px">is more useful than</div><div class="tile-line" style="left:11px;top:52px;font-size:19px">Authority</div></div>
  <div class="abs tile gray" style="left:740px;width:171px"><div class="tile-line" style="left:6px;top:-2px;font-size:64px;letter-spacing:-4px;line-height:80px">BI</div><div class="tile-line" style="left:69px;top:27px;font-size:20px;line-height:21px">Business<br>Intelligence</div></div>
  <div class="abs tile blue" style="left:920px;width:81px">
    <div class="tile-line" style="left:4px;top:5px;font-size:12px;line-height:14px">not like</div>
    <div class="tile-line" style="left:3px;top:19px;font-size:20px;line-height:22px;letter-spacing:-.5px">building</div>
    <div class="tile-line" style="left:4px;top:40px;font-size:16px;line-height:18px">a house</div>
  </div>
</main>

<footer class="abs footer">
  <div class="abs" style="left:203px;top:40px;display:flex;align-items:center;gap:8px"><span style="font-size:17px;letter-spacing:-.5px">KorvelPath</span><span style="width:11px;height:11px;border-radius:50%;background:#fff"></span></div>
  <p class="abs" style="left:200px;top:71px;font-size:11px">© 2013 KorvelPath</p>

  <div class="abs" style="left:390px;top:39px;width:395px">
    <h3>About Korvel Path</h3>
    <p style="margin-top:8px">Korvel Path provides technology services in a variety of areas. What makes us different is our focus on finding, training and retaining the very best people, who focus on providing our customers with the very best service.</p>
  </div>

  <div class="abs" style="left:814px;top:39px;width:200px">
    <h3>Contact</h3>
    <p style="margin-top:9px;font-size:11px">410 Linden Row, Harbor Falls, MN</p>
  </div>
  <span class="foot-social" style="left:815px" aria-label="Social link"></span>
  <span class="foot-social" style="left:852px" aria-label="Social link"></span>
  <span class="foot-social" style="left:888px" aria-label="Social link"></span>
  <span class="foot-social" style="left:925px" aria-label="Social link"></span>
  <span class="foot-social" style="left:961px" aria-label="Social link"></span>
</footer>

</body>
</html>
```